Yacht, Boats, Watersports company needs a redesign of business card

Hello Designers!
We are a Boat dealership company that sells fun in the water, we sell boats, Yachts, Kayaks and also yacht WaterSport toys. We are looking to redesign our business cards in to something a little bit more sophisticated. in a way that we can make better use of our company colors. I'm attaching a zipped file containing the company 3 sets of company logo which one is an horizontal another one is a vertical and also a chromed 3d logo. Also is included two set of business cards that we use and also some designs that i think it's interesting. We use PMS 2026c Orange and PMS 7687C Blue. I would like to see at least two different options with the orange as accent and also using blue as an accent color. It's really important for the business cards to have a font option and size that is legible to most people. Our current website is wwww.corvellamarine.com. Please visit if you want to have a better feeling of the Boat dealership
You can send Single sided or double side options. We are now using single sided but we may be open for a double side option if we really like the design.
Target Market(s)
Marine, boat sales, yacht sales, water toys sales/
Contact Information for Business Card
Name: Dale Pritchett
Address: 718 West Halden Lane,
Dania Beach, FL 33019
Phone: 954-382-7146
Fax: 954:382-7139
Cell: 954-451-8320
Email: 212@corvellamarine.com
Website: corvellamarine.com
Requirements
Must have
- the current information of the business card provided.
logo
use the PMS Colors
Nice to have
- a touch of elegance and sophistication but simple
Should not have
- should not have any typography that is hard to read, the card should be simple but yet sophisticated.

```html
<!DOCTYPE html>
<html lang="en">
<head>
<meta charset="utf-8">
<title>Corvella Marine – Business Card</title>
<link href="https://fonts.googleapis.com/css2?family=Work+Sans:wght@400;500;600&display=swap" rel="stylesheet">
<style>
  :root {
    --page-bg: #e9e6e1;
    --card-clear: #dfe5ea;
    --brand-blue: #1d4f86;
    --brand-blue-deep: #123a66;
    --brand-orange: #e8582a;
    --text-light: #f3f5f8;
  }
  * { margin: 0; padding: 0; box-sizing: border-box; }
  html, body {
    width: 1200px; height: 887px; overflow: hidden;
    background: var(--page-bg);
    font-family: "Work Sans", Arial, sans-serif;
  }
  .card {
    position: absolute; left: 75px; top: 143px;
    width: 1050px; height: 600px;
    border-radius: 26px; overflow: hidden;
    background: var(--card-clear);
    box-shadow: 0 10px 30px rgba(0,0,0,0.18);
  }
  .card-art { position: absolute; inset: 0; }
  .brand {
    position: absolute; left: 0; width: 480px; top: 42px;
    display: flex; flex-direction: column; align-items: center; gap: 14px;
  }
  .brand-dot {
    width: 72px; height: 72px; border-radius: 50%;
    border: 6px solid var(--brand-orange);
  }
  .brand-name {
    color: var(--text-light); font-weight: 600;
    font-size: 23px; letter-spacing: 2px; text-transform: uppercase;
  }
  .feature-name {
    position: absolute; left: 476px; top: 270px; width: 540px;
    text-align: center;
    color: var(--brand-blue-deep); font-weight: 600;
    font-size: 46px; line-height: 60px; letter-spacing: 3px; text-transform: uppercase;
  }
  .contact { position: absolute; left: 53px; top: 238px; color: var(--text-light); }
  .contact-name {
    color: var(--brand-orange); font-weight: 500;
    font-size: 40px; letter-spacing: 0.5px; text-transform: uppercase;
    margin-bottom: 10px;
  }
  .address { font-size: 24px; line-height: 32px; letter-spacing: 0.6px; margin-bottom: 10px; }
  .lines { list-style: none; }
  .lines li {
    display: flex; align-items: center; gap: 9px;
    font-size: 24px; line-height: 32px; letter-spacing: 0.6px;
  }
  .lines svg { width: 16px; height: 16px; flex: none; fill: none; stroke: var(--brand-orange); stroke-width: 2; }
</style>
</head>
<body>
  <div class="card">
    <svg class="card-art" viewBox="0 0 1050 600" aria-hidden="true">
      <rect x="0" y="0" width="746" height="600" fill="var(--brand-blue)"/>
      <circle cx="746" cy="300" r="276" fill="var(--card-clear)" stroke="var(--brand-blue-deep)" stroke-width="36"/>
    </svg>

    <div class="brand">
      <span class="brand-dot"></span>
      <span class="brand-name">Corvella Marine</span>
    </div>

    <p class="feature-name">Corvella Marine</p>

    <div class="contact">
      <h1 class="contact-name">Dale Pritchett</h1>
      <p class="address">718 West Halden Lane,<br>Dania Beach, FL 33019</p>
      <ul class="lines">
        <li><svg viewBox="0 0 16 16"><path d="M4 2 L6 5 L5 7 C6 9 7 10 9 11 L11 10 L14 12 L12 14 C7 14 2 9 2 4 Z"/></svg>954-382-7146</li>
        <li><svg viewBox="0 0 16 16"><rect x="4" y="2" width="8" height="4"/><rect x="2" y="6" width="12" height="6"/><rect x="4" y="10" width="8" height="4"/></svg>954:382-7139</li>
        <li><svg viewBox="0 0 16 16"><rect x="4" y="1.5" width="8" height="13" rx="1.5"/><path d="M7 12 H9"/></svg>954-451-8320</li>
        <li><svg viewBox="0 0 16 16"><rect x="1.5" y="3.5" width="13" height="9"/><path d="M1.5 3.5 L8 9 L14.5 3.5"/></svg>212@corvellamarine.com</li>
        <li><svg viewBox="0 0 16 16"><circle cx="8" cy="8" r="6.5"/><path d="M1.5 8 H14.5 M8 1.5 C5 5 5 11 8 14.5 M8 1.5 C11 5 11 11 8 14.5"/></svg>www.corvellamarine.com</li>
      </ul>
    </div>
  </div>
</body>
</html>
```